Need a flyer overhaul and minor changes

flyer is 5.5" x 8.5" we need to change the $250.00 to $325.00, update our company logo on the brochure, and also have an area where we can have the store address (318 W Harlan Ave, Del Rio, TX 78840 - (830) 642-9158). I've attached a our current brochure and our updated logo and we just want to make look better and updated.

Industry/Entity Type

Lending and Finance

Requirements
Nice to have
• updated layout and pictures

```html
<!DOCTYPE html>
<html lang="en">
<head>
<meta charset="utf-8">
<title>Harlan Lending Group – Title Loan Flyer</title>
<link rel="stylesheet" href="https://fonts.googleapis.com/css2?family=Montserrat:wght@700;800;900&family=Open+Sans:wght@400;600;700&display=swap">
<style>
  :root {
    --red: #e41f2b;
    --green-dark: #17582d;
    --green-text: #1e6a36;
    --mint: #bfe2cf;
    --ink-gray: #4b4b4b;
    --ink: #1d1d1d;
    --white: #ffffff;
    --stage: #ecebe8;
  }
  * { margin: 0; padding: 0; box-sizing: border-box; }
  html, body {
    width: 1096px; height: 1200px; overflow: hidden;
    background: var(--stage);
    font-family: "Open Sans", Arial, sans-serif;
  }
  .flyer {
    position: absolute; left: 179px; top: 31px;
    width: 464px; height: 716px;
    transform: scale(1.59); transform-origin: top left;
    background: var(--white); overflow: hidden;
  }
  .flyer > * { position: absolute; }
  .hero-photo {
    left: 196px; top: 0; width: 268px; height: 380px;
    background: radial-gradient(ellipse at 55% 30%, #e9d8c8 0%, #cdb8a3 22%, #d7e1ec 45%, #9fb4cf 75%, #eef1f5 100%);
  }
  .backdrop { left: 0; top: 0; width: 464px; height: 716px; }
  .headline-lead {
    left: 22px; top: 44px;
    font-family: "Montserrat", Arial, sans-serif; font-weight: 800;
    font-size: 38px; color: var(--ink-gray); letter-spacing: -0.01em;
  }
  .headline-main {
    left: 20px; top: 100px;
    font-family: "Montserrat", Arial, sans-serif; font-weight: 900;
    font-size: 80px; line-height: 66px; color: var(--red);
    letter-spacing: -0.085em; text-transform: uppercase;
  }
  .comparison {
    left: 25px; top: 260px; width: 262px; height: 382px;
    background: var(--white); border: 3px solid var(--red); border-radius: 16px;
    overflow: hidden;
  }
  .comparison-title {
    height: 26px; background: var(--red); color: var(--white);
    font-weight: 700; font-size: 12.5px; letter-spacing: 0.04em;
    display: flex; align-items: center; justify-content: center;
  }
  .comparison-heads {
    display: grid; grid-template-columns: 1fr 1fr; height: 44px;
    border-bottom: 1px solid var(--red); align-items: center;
  }
  .brand-small {
    font-family: "Montserrat", Arial, sans-serif; font-weight: 700;
    font-size: 9px; color: var(--green-dark); text-align: center; padding-right: 24px;
  }
  .col-title { font-weight: 700; font-size: 16px; color: var(--green-dark); padding-left: 10px; }
  .comparison-body {
    position: relative; display: grid; grid-template-columns: 1fr 1fr;
    padding-top: 10px; height: 252px;
  }
  .comparison-body::after {
    content: ""; position: absolute; left: 50%; top: 0; bottom: 0;
    width: 1px; background: var(--red);
  }
  .schedule { list-style: none; padding-left: 12px; }
  .schedule li {
    display: flex; font-size: 13.5px; line-height: 19.6px; color: var(--green-text);
  }
  .schedule .month { width: 32px; }
  .comparison-foot {
    position: absolute; left: 0; right: 0; bottom: 0; height: 56px;
    background: var(--red); color: var(--white);
    display: grid; grid-template-columns: 1fr 1fr; font-weight: 700;
  }
  .comparison-foot div { padding: 8px 0 0 14px; font-size: 14.5px; line-height: 18px; }
  .comparison-foot small { display: block; font-size: 13px; padding-left: 2px; }
  .brand-main {
    left: 300px; top: 356px; width: 160px; text-align: center;
    font-family: "Montserrat", Arial, sans-serif; font-weight: 700;
    font-size: 19px; line-height: 22px; color: var(--green-dark);
  }
  .contact { left: 304px; top: 452px; width: 150px; }
  .contact-title { font-weight: 700; font-size: 14.5px; color: var(--ink); margin-bottom: 14px; }
  .contact-rule { position: relative; height: 1px; background: var(--red); margin: 0 0 9px; }
  .contact-rule svg { position: absolute; left: 67px; top: -7px; background: var(--mint); padding: 0 2px; }
  .contact-line { font-size: 12.5px; line-height: 17px; color: var(--ink); text-align: center; margin-bottom: 14px; }
  .spanish-note {
    left: 18px; top: 675px; font-weight: 700; font-size: 13px;
    color: var(--red); letter-spacing: 0.01em;
  }
  .phone {
    left: 200px; top: 659px; font-weight: 600; font-size: 30px;
    color: var(--white); letter-spacing: 0.02em;
  }
</style>
</head>
<body>
<main class="flyer">
  <div class="hero-photo" role="img" aria-label="Photo of a delighted woman holding cash and dropping a bill into a pink piggy bank"></div>

  <svg class="backdrop" viewBox="0 0 464 716" width="464" height="716" aria-hidden="true">
    <path d="M0 364 C140 352 290 330 464 276 L464 716 L0 716 Z" fill="var(--red)"/>
    <path d="M0 372 C140 360 290 338 464 284 L464 716 L0 716 Z" fill="var(--mint)"/>
    <path d="M0 620 C150 636 320 606 464 594 L464 716 L0 716 Z" fill="var(--red)"/>
    <path d="M0 632 C150 648 320 618 464 606 L464 716 L0 716 Z" fill="var(--green-dark)"/>
  </svg>

  <p class="headline-lead">STUCK in a</p>
  <h1 class="headline-main">Title<br>Loan?</h1>

  <section class="comparison">
    <div class="comparison-title">$1,000 LOAN COMPARISON</div>
    <div class="comparison-heads">
      <div class="brand-small">Harlan Lending</div>
      <div class="col-title">TITLE LOAN</div>
    </div>
    <div class="comparison-body">
      <ol class="schedule">
        <li><span class="month">1</span>$131.67</li><li><span class="month">2</span>$131.67</li>
        <li><span class="month">3</span>$131.67</li><li><span class="month">4</span>$131.67</li>
        <li><span class="month">5</span>$131.67</li><li><span class="month">6</span>$131.67</li>
        <li><span class="month">7</span>$131.67</li><li><span class="month">8</span>$131.67</li>
        <li><span class="month">9</span>$131.67</li><li><span class="month">10</span>$131.67</li>
        <li><span class="month">11</span>$131.67</li><li><span class="month">12</span>$131.67</li>
      </ol>
      <ol class="schedule">
        <li><span class="month">1</span>$325.00</li><li><span class="month">2</span>$325.00</li>
        <li><span class="month">3</span>$325.00</li><li><span class="month">4</span>$325.00</li>
        <li><span class="month">5</span>$325.00</li><li><span class="month">6</span>$325.00</li>
        <li><span class="month">7</span>$325.00</li><li><span class="month">8</span>$325.00</li>
        <li><span class="month">9</span>$325.00</li><li><span class="month">10</span>$325.00</li>
        <li><span class="month">11</span>$325.00</li><li><span class="month">12</span>$325.00</li>
      </ol>
    </div>
    <div class="comparison-foot">
      <div>PAID OFF</div>
      <div>STILL OWE<small>$1,000</small></div>
    </div>
  </section>

  <div class="brand-main">Harlan Lending<br>Group</div>

  <address class="contact" style="font-style: normal;">
    <p class="contact-title">Contact Us</p>
    <div class="contact-rule">
      <svg width="14" height="14" viewBox="0 0 14 14" aria-hidden="true">
        <path d="M7 1a4 4 0 0 0-4 4c0 3 4 8 4 8s4-5 4-8a4 4 0 0 0-4-4z" fill="var(--red)"/>
        <circle cx="7" cy="5" r="1.5" fill="var(--mint)"/>
      </svg>
    </div>
    <p class="contact-line">318 W Harlan Ave, Del<br>Rio, TX 78840</p>
    <div class="contact-rule">
      <svg width="14" height="14" viewBox="0 0 14 14" aria-hidden="true">
        <circle cx="6" cy="6" r="4.5" fill="none" stroke="var(--red)" stroke-width="1.5"/>
        <path d="M1.5 6h9M6 1.5c-2 2.5-2 6.5 0 9M6 1.5c2 2.5 2 6.5 0 9" fill="none" stroke="var(--red)" stroke-width="1"/>
        <path d="M8 8l5 2-2 1-1 2z" fill="var(--red)"/>
      </svg>
    </div>
    <p class="contact-line">www.harlanlending.com</p>
  </address>

  <p class="spanish-note">SE HABLA ESPAÑOL</p>
  <p class="phone">(830) 642-9158</p>
</main>
</body>
</html>
```